Design a Flyer for Super Hero Day

Looking for a unique/cool flyer design for a kids super hero party.

I'll need an 8.5x11 flyer and a 4x6 matching in style image.

This should say: Fighting for Justice! Pursuing the Good! Striving for Awesome!

For any photos/images you need please use www.Pictovane.com I will purchase and attach any images for the winning designer. In the meantime, simply take a screen shot of the image you'd like to use, I understand the watermarks will be there, that's okay, we'll purchase the winning photos at the end.

Suggestions: Cool comic book style, maybe, mixed with a reality picture of a real kid?

I will need all photoshop work/source files in case there needs to be any edits, changes. There should be a space for a logo/day/date/time information. I appreciate if this can be incorporated INTO the design someway, and not just "added" if that makes sense.

Also, if you have questions post for clarification, I'll be quick to reply. Thank you :)

```html
<!DOCTYPE html>
<html lang="en">
<head>
<meta charset="utf-8">
<title>Superhero Party Flyer</title>
<link rel="stylesheet" href="https://fonts.googleapis.com/css2?family=Lilita+One&family=Orbitron:wght@900&display=swap">
<style>
  :root {
    --night: #020202;
    --hero-red: #e4242b;
    --band-red: #de2f3a;
    --lime: #c8f21c;
    --slogan-green: #2cf23a;
    --slogan-edge: #c4161c;
    --sun-core: #f7c21a;
    --sun-glow: #e8a20f;
    --water-blue: #3f78b8;
    --water-foam: #b9cde0;
  }
  html, body {
    margin: 0;
    padding: 0;
    overflow: hidden;
    background: var(--night);
  }
  .flyer {
    position: relative;
    width: 927px;
    height: 1200px;
    overflow: hidden;
    background: var(--night);
    font-family: "Lilita One", "Arial Black", sans-serif;
  }
  .halftone-field {
    position: absolute;
    left: 0;
    top: 0;
    width: 420px;
    height: 980px;
    background: radial-gradient(ellipse 70% 75% at 0% 25%, #c81d24 0%, #8e1016 40%, rgba(60, 6, 8, 0.55) 70%, rgba(2, 2, 2, 0) 100%);
  }
  .sun-burst {
    position: absolute;
    left: 660px;
    top: -40px;
    width: 360px;
    height: 460px;
    background: radial-gradient(ellipse 50% 50% at 55% 45%, var(--sun-core) 0%, var(--sun-glow) 35%, rgba(232, 162, 15, 0.45) 62%, rgba(2, 2, 2, 0) 100%);
  }
  .water-splash {
    position: absolute;
    left: -120px;
    top: 700px;
    width: 720px;
    height: 400px;
    background: radial-gradient(ellipse 50% 50% at 50% 60%, var(--water-foam) 0%, var(--water-blue) 40%, rgba(30, 60, 100, 0.5) 70%, rgba(2, 2, 2, 0) 100%);
  }
  .hero-photo {
    position: absolute;
    left: 30px;
    top: 235px;
    width: 670px;
    height: 600px;
    border-radius: 44% 38% 30% 40%;
    background: linear-gradient(160deg, #e9b53a 0%, #d8322c 40%, #3f6fc4 72%, #f0bf2e 100%);
    box-shadow: 0 0 22px rgba(255, 238, 170, 0.55);
  }
  .slogans {
    position: absolute;
    right: 295px;
    top: 30px;
    margin: 0;
    text-align: right;
    font-size: 50px;
    line-height: 57px;
    font-variant: small-caps;
    color: var(--slogan-green);
    -webkit-text-stroke: 3px var(--slogan-edge);
    paint-order: stroke fill;
    letter-spacing: 0.5px;
  }
  .slogans span { display: block; }
  .event-title {
    position: absolute;
    left: 0;
    top: 0;
    width: 927px;
    height: 1060px;
    font-family: "Orbitron", "Arial Black", sans-serif;
    font-weight: 900;
  }
  .title-main { fill: var(--lime); stroke: #4a3a00; stroke-width: 2px; paint-order: stroke fill; }
  .title-sub { fill: var(--hero-red); stroke: #5a0508; stroke-width: 2px; paint-order: stroke fill; }
  .info-band {
    position: absolute;
    left: 0;
    top: 1058px;
    width: 927px;
    height: 142px;
    background: linear-gradient(180deg, #e5343f 0%, var(--band-red) 60%, #c9222d 100%);
    color: var(--lime);
  }
  .event-details {
    position: absolute;
    left: 5px;
    top: 24px;
    margin: 0;
    font-size: 38px;
    line-height: 43px;
    font-variant: small-caps;
  }
  .event-details dt { margin: 0; }
  .event-details .location { padding-left: 14px; }
  .host-mark {
    position: absolute;
    left: 736px;
    top: 44px;
    font-size: 52px;
    line-height: 1;
    font-variant: small-caps;
  }
</style>
</head>
<body>
<div class="flyer">
  <div class="halftone-field" role="img" aria-label="Red comic-book halftone dot pattern"></div>
  <div class="sun-burst" role="img" aria-label="Eclipsed sun with crackling yellow lightning rays"></div>
  <div class="water-splash" role="img" aria-label="Splashing blue water wave"></div>
  <div class="hero-photo" role="img" aria-label="Photo of a child in a red, blue and yellow superhero costume with a cape, striking a pointing pose"></div>

  <p class="slogans">
    <span>Fighting for Justice!</span>
    <span>Pursuing the Good!</span>
    <span>Striving for Awesome!</span>
  </p>

  <svg class="event-title" viewBox="0 0 927 1060" aria-label="Superhero Party">
    <text class="title-main" x="42" y="916" font-size="112" textLength="864" lengthAdjust="spacingAndGlyphs">SUPERHERO</text>
    <text class="title-sub" x="412" y="1003" font-size="98" textLength="502" lengthAdjust="spacingAndGlyphs">PARTY</text>
  </svg>

  <footer class="info-band">
    <dl class="event-details">
      <dt>Date/Time:</dt>
      <dt class="location">Location:</dt>
    </dl>
    <div class="host-mark">Logo</div>
  </footer>
</div>
</body>
</html>
```